Book Cover : Silent Tides: Protein Engines and the Cellular Horizon

We need a striking and engaging book cover for this new book which describes the development of the COVID-19 vaccine technology and it's potential to change the world in ways which most people don't yet realise.

On the book cover we need to include:

Silent Tides: Protein Engines and the Cellular Horizon

Safety/Efficiency/Future Applications/CRISPR

Tadeusz Głowik

Need extra days to review

```html
<!DOCTYPE html>
<html lang="en">
<head>
<meta charset="utf-8">
<title>Silent Tides: Protein Engines and the Cellular Horizon — Book Cover Wrap</title>
<link rel="stylesheet" href="https://fonts.googleapis.com/css2?family=Fredoka:wght@600;700&family=Montserrat:ital,wght@0,400;0,800;1,700&display=swap">
<style>
  :root {
    --stage: #eeeeee;
    --paper: #ffffff;
    --ink: #0b0b0b;
    --accent: #1a7fe6;
    --tint: #bfe4f4;
    --tint-soft: #e6f5fb;
    --steel-light: #f3f4f5;
    --steel-mid: #d8dadc;
  }
  * { box-sizing: border-box; margin: 0; padding: 0; }
  html, body {
    width: 899px; height: 1200px; overflow: hidden;
    background: var(--stage);
  }
  .canvas { position: relative; width: 899px; height: 1200px; }

  .wrap {
    position: absolute; left: 20px; top: 303px;
    width: 859px; height: 596px;
    background: var(--paper);
    overflow: hidden;
    box-shadow: 0 2px 8px rgba(0,0,0,.18);
  }

  /* back cover */
  .back {
    position: absolute; left: 0; top: 0; width: 413px; height: 100%;
    background:
      radial-gradient(ellipse 360px 300px at 10% 92%, var(--tint) 0%, var(--tint-soft) 55%, rgba(255,255,255,0) 100%),
      linear-gradient(90deg, var(--tint-soft) 0%, var(--paper) 85%);
  }
  .back-syringe {
    position: absolute; left: 0; top: 48px; width: 337px; height: 40px;
    background: linear-gradient(90deg, var(--steel-mid) 0%, var(--steel-light) 100%);
  }
  .back-virus {
    position: absolute; left: 0; top: 330px; width: 300px; height: 266px;
    background: radial-gradient(ellipse at 30% 70%, rgba(150,205,230,.55), rgba(255,255,255,0) 70%);
  }
  .blurb {
    position: absolute; left: 42px; top: 128px; width: 305px;
    font-family: "Montserrat", sans-serif; font-size: 10.4px; line-height: 13.3px;
    color: var(--ink); text-align: justify;
  }
  .blurb p + p { margin-top: 13px; }
  .barcode-box {
    position: absolute; left: 271px; top: 508px; width: 78px; height: 60px;
    background: var(--paper);
  }

  /* spine */
  .spine { position: absolute; left: 413px; top: 0; width: 49px; height: 100%; }
  .spine-title, .spine-author {
    position: absolute; left: 50%; transform: translateX(-50%);
    writing-mode: vertical-rl; white-space: nowrap;
  }
  .spine-title {
    top: 22px; font-family: "Fredoka", sans-serif; font-weight: 700;
    font-size: 13.6px; color: var(--accent);
  }
  .spine-author {
    top: 462px; font-family: "Montserrat", sans-serif; font-weight: 800;
    font-size: 13px; color: var(--ink);
  }

  /* front cover */
  .front { position: absolute; left: 462px; top: 0; width: 397px; height: 100%; }
  .front-syringe {
    position: absolute; left: -31px; top: 0; width: 72px; height: 640px;
    transform-origin: 50% 0; transform: rotate(-17deg);
    background: linear-gradient(90deg, var(--steel-light) 0%, var(--steel-mid) 100%);
  }
  .title {
    position: absolute; right: 46px; top: 54px;
    font-family: "Fredoka", sans-serif; font-weight: 700; color: var(--ink);
    text-align: right; line-height: 1;
  }
  .title span { display: block; }
  .title-lead { font-size: 82px; letter-spacing: -2px; }
  .title-mid { font-size: 50px; margin-top: 2px; }
  .title-sub { font-size: 30px; margin-top: 6px; }
  .topics {
    position: absolute; right: 46px; top: 352px; list-style: none;
    font-family: "Montserrat", sans-serif; font-style: italic; font-weight: 700;
    font-size: 14px; line-height: 23px; color: var(--accent); text-align: right;
  }
  .topics li:nth-child(1) { margin-right: 6px; }
  .topics li:nth-child(3) { margin-right: 10px; }
  .author {
    position: absolute; right: 40px; top: 538px;
    font-family: "Montserrat", sans-serif; font-weight: 800;
    font-size: 31px; color: var(--ink); white-space: nowrap;
  }
</style>
</head>
<body>
<main class="canvas">
  <section class="wrap">

    <div class="back">
      <div class="back-syringe" role="img" aria-label="Photograph of a syringe lying horizontally, needle pointing right"></div>
      <div class="back-virus" role="img" aria-label="Faint pale blue virus particles illustration"></div>
      <div class="blurb">
        <p>Lorem ipsum dolor sit amet, consectetur adipiscing elit. Curabitur finibus placerat malesuada. Aenean a nulla eget orci tristique molestie. Pellentesque nec velit molestie, malesuada purus nec, tincidunt tortor. Morbi et varius justo. Etiam tortor tortor, maximus id convallis eget, rhoncus vel orci. Aenean quis sem eu tortor feugiat consequat id mattis orci. Phasellus massa augue, bibendum sit amet elementum sed, malesuada a nulla. Integer et placerat sapien. Mauris venenatis, ex vulputate consequat venenatis, ante arcu placerat diam, a porttitor ipsum est aliquet justo. Praesent sodales metus eu felis dictum lacinia. Donec ac consequat nunc, imperdiet vehicula justo. In sollicitudin convallis lorem, vel iaculis velit pellentesque rhoncus. Pellentesque dapibus odio vitae justo ornare, ac condimentum nunc laoreet.</p>
        <p>Orci varius natoque penatibus et magnis dis parturient montes, nascetur ridiculus mus. Duis a elementum erat. Nulla facilisi. Suspendisse id vulputate ligula, eu iaculis lacus. Donec ac mollis odio. Sed purus leo, sagittis at felis sit amet, convallis ultrices est. Donec augue mi, consectetur sed nunc sed, molestie aliquet lectus. Donec ut tempus neque. Praesent orci sem, dapibus sed tempus ut, laoreet at nisi. Duis vel ex et mauris euismod tristique vel ut urna. Donec commodo</p>
      </div>
      <div class="barcode-box"></div>
    </div>

    <div class="spine">
      <span class="spine-title">Silent Tides: Protein Engines and the Cellular Horizon</span>
      <span class="spine-author">TADEUSZ GŁOWIK</span>
    </div>

    <div class="front">
      <div class="front-syringe" role="img" aria-label="Photograph of a large syringe leaning diagonally across the cover, needle at top"></div>
      <h1 class="title">
        <span class="title-lead">Silent</span>
        <span class="title-mid">Tides:</span>
        <span class="title-mid">Protein</span>
        <span class="title-sub">Engines and the</span>
        <span class="title-sub">Cellular Horizon</span>
      </h1>
      <ul class="topics">
        <li>Safety</li>
        <li>Efficiency</li>
        <li>Future Applications</li>
        <li>CRISPR</li>
      </ul>
      <p class="author">TADEUSZ GŁOWIK</p>
    </div>

  </section>
</main>
</body>
</html>
```